Business card design needed

Our modern electrical contracting company requires business card design utilising our logo and incorporating our tag line "Service when you need it". We specialise in assisting our customers 24/7 offering a breakdown service.

Industry/Entity Type

Electrical

Contact Information for Business Card

Marcus Penhale, Electrical contractor,Tel: (08) 8456 3071, Fax: (08) 8679 4315, Mob 0438 562 740, Email: marcus.penhale@brightwirepower.com.au, Web: www.brightwirepower.com.au

Requirements
Must have
• we require a 2 sided card.
Front- Logo, tag line and contact information.
Rear- service when you need it! Call now for our 24/7 breakdown service

```html
<!DOCTYPE html>
<html lang="en">
<head>
<meta charset="utf-8">
<title>Brightwire Power Business Cards</title>
<link rel="stylesheet" href="https://fonts.googleapis.com/css2?family=Ubuntu:wght@400;500;700&display=swap">
<style>
  :root {
    --page-bg: #e6e7ea;
    --card-white: #ffffff;
    --card-tint: #eceef1;
    --brand-blue: #1c5fd4;
    --sky-blue: #1aa9ec;
    --navy: #0c2c8c;
    --ink: #161616;
    --ink-soft: #3a3a3a;
  }
  * { box-sizing: border-box; margin: 0; padding: 0; }
  html, body { width: 1200px; height: 861px; overflow: hidden; }
  body {
    background: var(--page-bg);
    font-family: "Ubuntu", sans-serif;
    color: var(--ink);
    position: relative;
  }
  .card {
    position: absolute;
    top: 270px;
    width: 520px;
    height: 320px;
    background: linear-gradient(180deg, var(--card-white) 0%, var(--card-tint) 100%);
    box-shadow: 0 6px 18px rgba(0,0,0,0.18);
    overflow: hidden;
  }
  .card--front { left: 50px; }
  .card--back { left: 630px; }

  .card__band {
    position: absolute;
    top: 0;
    width: 14px;
    height: 100%;
    background: linear-gradient(180deg, var(--sky-blue) 0%, var(--brand-blue) 50%, var(--navy) 100%);
  }
  .card__band--left { left: 0; }
  .card__band--right { right: 0; }

  .brand {
    position: absolute;
    left: 0; right: 0;
    display: flex;
    flex-direction: column;
    align-items: center;
  }
  .brand__disc {
    border-radius: 50%;
    background: var(--brand-blue);
  }
  .brand__name {
    font-family: "Ubuntu", sans-serif;
    font-weight: 700;
    color: var(--brand-blue);
    white-space: nowrap;
    line-height: 1;
  }
  .card--front .brand { top: 14px; }
  .card--front .brand__disc { width: 64px; height: 64px; margin-bottom: 20px; }
  .card--front .brand__name { font-size: 25px; }
  .card--back .brand { top: 28px; }
  .card--back .brand__disc { width: 82px; height: 82px; margin-bottom: 30px; }
  .card--back .brand__name { font-size: 33px; }

  .holder {
    position: absolute;
    top: 152px;
    left: 0; right: 0;
    text-align: center;
  }
  .holder__name {
    font-weight: 700;
    font-size: 31px;
    letter-spacing: -1px;
    line-height: 1;
  }
  .holder__role {
    margin-top: 3px;
    font-weight: 500;
    font-size: 13px;
    color: var(--navy);
  }

  .contacts {
    position: absolute;
    list-style: none;
    font-size: 14.5px;
    font-weight: 500;
    color: var(--ink-soft);
  }
  .contacts--phones { left: 38px; top: 206px; }
  .contacts--online { left: 178px; top: 222px; }
  .contacts li {
    display: flex;
    align-items: center;
    gap: 7px;
    height: 26px;
    white-space: nowrap;
  }
  .contacts svg { width: 16px; height: 16px; flex: none; }

  .tagline {
    position: absolute;
    top: 224px;
    left: 0; right: 0;
    text-align: center;
    font-weight: 700;
    font-size: 26px;
    letter-spacing: -0.8px;
  }
  .call-line {
    position: absolute;
    top: 262px;
    left: 0; right: 0;
    text-align: center;
    font-weight: 500;
    font-size: 21px;
    color: var(--navy);
  }
</style>
</head>
<body>

<section class="card card--front" aria-label="Card front">
  <span class="card__band card__band--left"></span>
  <span class="card__band card__band--right"></span>

  <div class="brand">
    <span class="brand__disc"></span>
    <span class="brand__name">BRIGHTWIRE POWER</span>
  </div>

  <div class="holder">
    <p class="holder__name">Marcus Penhale</p>
    <p class="holder__role">Electrical Contractor</p>
  </div>

  <ul class="contacts contacts--phones">
    <li>
      <svg viewBox="0 0 16 16" aria-hidden="true"><circle cx="8" cy="8" r="8" fill="#2a2a2a"/><path d="M5 4l2 0.6-0.6 2 2.9 2.9 2-0.6 0.7 2-1.5 1.2C7.5 12 4 8.5 3.9 5.5z" fill="#fff"/></svg>
      (08) 8456 3071
    </li>
    <li>
      <svg viewBox="0 0 16 16" aria-hidden="true"><circle cx="8" cy="8" r="8" fill="#2a2a2a"/><rect x="5" y="3.5" width="6" height="3" fill="#fff"/><rect x="3.5" y="6.5" width="9" height="4" rx="1" fill="#fff"/><rect x="5" y="10" width="6" height="2.5" fill="#fff"/></svg>
      (08) 8679 4315
    </li>
    <li>
      <svg viewBox="0 0 16 16" aria-hidden="true"><circle cx="8" cy="8" r="8" fill="#2a2a2a"/><rect x="5.5" y="3" width="5" height="10" rx="1" fill="#fff"/><rect x="6.5" y="4.3" width="3" height="5" fill="#2a2a2a"/></svg>
      0438 562 740
    </li>
  </ul>

  <ul class="contacts contacts--online">
    <li>
      <svg viewBox="0 0 16 16" aria-hidden="true"><circle cx="8" cy="8" r="8" fill="#2a2a2a"/><rect x="3.5" y="5" width="9" height="6.5" fill="#fff"/><path d="M3.5 5l4.5 3.6L12.5 5" stroke="#2a2a2a" stroke-width="1" fill="none"/></svg>
      marcus.penhale@brightwirepower.com.au
    </li>
    <li>
      <svg viewBox="0 0 16 16" aria-hidden="true"><circle cx="8" cy="8" r="8" fill="#2a2a2a"/><rect x="3.5" y="4" width="9" height="6" fill="#fff"/><rect x="6.5" y="10.5" width="3" height="1.5" fill="#fff"/></svg>
      www.brightwirepower.com.au
    </li>
  </ul>
</section>

<section class="card card--back" aria-label="Card back">
  <span class="card__band card__band--left"></span>
  <span class="card__band card__band--right"></span>

  <div class="brand">
    <span class="brand__disc"></span>
    <span class="brand__name">BRIGHTWIRE POWER</span>
  </div>

  <p class="tagline">Service when you need it!</p>
  <p class="call-line">Call now for our 24/7 breakdown service</p>
</section>

</body>
</html>
```